Digital Menu Board for Restaurant

I want a digital menu board for our new restaurant. I have provided the sample of what I kind of want.
This is to be on a 55 inch tv so it needs to be the correct aspect ratio of 4:5

Font styles to use
Serif
Sans Serif

Colors
f59296
f04a50
ec1f27
ffffff
fffef7
fbed22
ffc214
0592cd
e5519f

Requirements
Must have
• fun, maybe something moving? bright colors on a darker background so it's easy to read or dark font on a light background.

```html
<!DOCTYPE html>
<html lang="en">
<head>
<meta charset="utf-8">
<title>Sandy Coves Menu Board</title>
<link rel="stylesheet" href="https://fonts.googleapis.com/css2?family=Open+Sans:ital,wght@0,400;0,600;0,700;0,800;1,400;1,600;1,700&display=swap">
<style>
  :root {
    --navy: #2e3192;
    --ink: #2b3467;
    --text: #333340;
    --white: #ffffff;
    --cream: #fffef7;
    --red: #f04a50;
    --red-deep: #ec1f27;
    --rose: #f59296;
    --pink-soft: #f8c9cb;
    --yellow: #fbed22;
    --yellow-soft: #fbf49e;
    --gold: #ffc214;
    --orange: #f7944a;
    --blue: #0592cd;
    --blue-soft: #d3e9ec;
    --magenta: #e5519f;
  }
  * { box-sizing: border-box; margin: 0; padding: 0; }
  html, body { width: 961px; height: 1200px; overflow: hidden; background: var(--white); }
  .board {
    position: relative;
    width: 961px;
    height: 1200px;
    overflow: hidden;
    background: var(--white);
    font-family: "Open Sans", sans-serif;
    color: var(--text);
  }
  .backdrop { position: absolute; inset: 0; width: 961px; height: 1200px; }

  .brand {
    position: absolute;
    left: 44px; top: 40px;
    width: 412px; height: 190px;
    display: flex; align-items: center; justify-content: center; gap: 14px;
  }
  .brand-dot { width: 30px; height: 30px; border-radius: 50%; background: var(--gold); }
  .brand-name {
    font-family: "Open Sans", sans-serif;
    font-weight: 800;
    font-size: 58px;
    color: var(--red);
    letter-spacing: -0.5px;
  }

  .combo {
    position: absolute;
    left: 572px; top: 47px;
    width: 322px; height: 189px;
    background: var(--red);
    border-radius: 44px 44px 60px 60px;
    text-align: center;
    color: var(--white);
    font-weight: 700;
    padding-top: 20px;
  }
  .combo-title { color: var(--yellow); font-size: 34px; font-weight: 700; line-height: 40px; }
  .combo-line { font-size: 23.5px; line-height: 35px; }

  .tag {
    position: absolute;
    height: 36px;
    background: var(--navy);
    color: var(--white);
    font-weight: 700;
    font-size: 19px;
    line-height: 36px;
    text-transform: uppercase;
    text-align: center;
    clip-path: polygon(0 0, 100% 0, calc(100% - 10px) 50%, 100% 100%, 0 100%, 10px 50%);
  }
  .tag-buns { left: 52px; top: 278px; width: 220px; }
  .tag-sides { left: 505px; top: 272px; width: 86px; }
  .tag-kids { left: 608px; top: 500px; width: 312px; }
  .tag-drinks { left: 505px; top: 711px; width: 134px; }
  .tag-shake { left: 794px; top: 920px; width: 123px; }

  .item { position: absolute; }
  .item-name { font-weight: 700; font-size: 19px; line-height: 24px; color: var(--ink); }
  .item-name sup { font-size: 11px; }
  .item-name.is-italic { font-style: italic; }
  .item-desc { font-style: italic; font-size: 14px; line-height: 21px; color: var(--text); margin-top: 2px; }
  .item-extra { font-style: italic; font-weight: 700; font-size: 14px; line-height: 21px; color: var(--text); }

  .list { position: absolute; list-style: none; font-size: 19px; line-height: 26.7px; color: var(--ink); }
  .list-right { text-align: right; }
  .list small { display: block; font-size: 11px; line-height: 14px; margin: -4px 0 2px; }

  .art { position: absolute; border-radius: 18px; }
  .art-burger { left: 0; top: 439px; width: 122px; height: 150px; background: linear-gradient(180deg, var(--gold), var(--orange)); border-radius: 0 50px 24px 0; }
  .art-fries { left: 778px; top: 322px; width: 89px; height: 145px; background: linear-gradient(180deg, var(--gold), var(--red-deep)); border-radius: 8px 8px 18px 18px; }
  .art-sandwich { left: 500px; top: 544px; width: 139px; height: 134px; background: linear-gradient(135deg, var(--orange), var(--red)); }
  .art-cup { left: 783px; top: 711px; width: 95px; height: 156px; background: linear-gradient(180deg, var(--magenta), #8fb4f0); border-radius: 12px 12px 22px 22px; }
  .art-shake { left: 478px; top: 994px; width: 94px; height: 173px; background: linear-gradient(180deg, var(--gold), var(--red)); border-radius: 10px 10px 16px 16px; }
</style>
</head>
<body>
<main class="board">
  <svg class="backdrop" viewBox="0 0 865 1080" aria-hidden="true">
    <path d="M0 0 H40 C48 40 30 90 18 120 C10 140 0 148 0 150 Z" fill="#d3e9ec"/>
    <path d="M600 0 H865 V330 C820 300 800 240 760 200 C720 160 660 120 620 70 C605 45 598 20 600 0 Z" fill="#fbf49e"/>
    <path d="M610 330 C660 300 760 300 865 340 V620 C800 640 720 610 660 560 C610 520 560 380 610 330 Z" fill="#d3e9ec"/>
    <path d="M0 470 C60 420 140 405 210 440 C280 475 340 470 400 500 C480 540 565 570 575 660 C585 745 520 800 470 850 C425 895 370 930 290 920 C220 912 140 900 80 880 C30 865 0 850 0 830 Z" fill="#f8c9cb"/>
    <path d="M740 880 C800 860 840 870 865 880 V1080 H660 C670 1010 690 920 740 880 Z" fill="#d3e9ec"/>
    <path d="M0 950 C50 940 110 960 140 1010 C155 1040 150 1065 145 1080 H0 Z" fill="#fbf49e"/>
  </svg>

  <div class="brand">
    <span class="brand-dot"></span>
    <span class="brand-name">Sandy Coves</span>
  </div>

  <section class="combo">
    <p class="combo-title">COMBO UP</p>
    <p class="combo-line">Add 1 side and drink</p>
    <p class="combo-line">Add 1 side and shake</p>
    <p class="combo-line">Additional Sides</p>
  </section>

  <h2 class="tag tag-buns">Between Buns</h2>

  <div class="art art-burger" role="img" aria-label="Burger icon goes here"></div>

  <article class="item" style="left:52px; top:321px;">
    <h3 class="item-name">1<sup>st</sup> Point Pulled Pork</h3>
    <p class="item-desc">Pulled Pork, Rick's Sassy BBQ Sauce, Chopped Bacon,<br>Pepperjack Cheese, and Fried Jalapeño Pepper on a<br>Ciabatta Bun</p>
  </article>

  <article class="item" style="left:119px; top:425px;">
    <h3 class="item-name">2<sup>nd</sup> Point Pulled Pork</h3>
    <p class="item-desc" style="padding-left:14px;">Pulled Pork, Rick's Sweet Raspberry BBQ<br>Sauce, and Coleslaw on a Ciabatta Bun</p>
  </article>

  <article class="item" style="left:109px; top:506px;">
    <h3 class="item-name" style="padding-left:38px;">Spiniker Point Burger</h3>
    <p class="item-desc" style="padding-left:37px;">Smokerhouse 1/2 Pound Burger,</p>
    <p class="item-desc" style="padding-left:21px; margin-top:0;">Crumbled Bacon, Rick's Sassy BBQ Sauce,</p>
    <p class="item-desc" style="padding-left:19px; margin-top:0;">Cheese, and Onion Rings</p>
    <p class="item-desc" style="margin-top:0;">on a Toasted Brioche Bun</p>
  </article>

  <article class="item" style="left:52px; top:631px;">
    <h3 class="item-name">The Rock Burger</h3>
    <p class="item-desc">Two Smokerhouse 1/2 Pound Patties, Cheese, Lettuce,<br>Tomato, Onion, Pickles on a Toasted Brioche Bun</p>
  </article>

  <article class="item" style="left:52px; top:712px;">
    <h3 class="item-name">Rainbow Cove Sandwich</h3>
    <p class="item-desc">Chicken Salad - Smoked Chicken, Celery and Onion<br>Mixed with Our BBQ Mayo and Topped with Seasoned<br>Tomato on a Hoagie Roll</p>
  </article>

  <article class="item" style="left:52px; top:815px;">
    <h3 class="item-name is-italic">North Beach Salad</h3>
    <p class="item-desc">Pulled Pork and Black Bean on a Bed Of Romaine,<br>Tomato and Onion with Sweet and Sour Raspberry<br>Pineapple Sauce.</p>
  </article>

  <article class="item" style="left:52px; top:917px;">
    <h3 class="item-name">West Side Salad</h3>
    <p class="item-desc">Bbq Pulled Pork, Crumbled Bacon, Candied Walnuts,<br>Feta Cheese, Red Onion, Spinach and Lecture with<br>Ranch Dressing or Raspberry Vinaigrette</p>
  </article>

  <article class="item" style="left:52px; top:1021px;">
    <h3 class="item-name">East Side Salad</h3>
    <p class="item-desc">Spinach and Lettuce, Chopped Apples, Candied<br>Walnuts, Onion, Feta Cheese with Rick's Rasberry<br>Vinaigrette</p>
    <p class="item-extra">Add Chicken</p>
  </article>

  <h2 class="tag tag-sides">Sides</h2>
  <ul class="list" style="left:504px; top:313px;">
    <li>Seasoned Fries</li>
    <li>Onion Rings</li>
    <li>Sweet Cornbread</li>
    <li>Sweet Coleslaw</li>
    <li>Macaroni Salad</li>
    <li>Side Salad</li>
  </ul>
  <div class="art art-fries" role="img" aria-label="Fries icon goes here"></div>

  <h2 class="tag tag-kids">Seashell Finders (Kids)</h2>
  <div class="art art-sandwich" role="img" aria-label="Sandwich icon goes here"></div>
  <ul class="list list-right" style="right:44px; top:543px;">
    <li>Little Cheeseburger</li>
    <li>Pulled Pork Sandwich</li>
    <li>Mini Corn Dogs</li>
    <li>Chicken Salad Sandwich</li>
    <li>Fries / Onion Rings</li>
  </ul>

  <h2 class="tag tag-drinks">Drinks</h2>
  <ul class="list" style="left:504px; top:753px; width:120px;">
    <li>Pep Fizz</li>
    <li>Diet Pep Fizz</li>
    <li>Kola</li>
    <li>Diet Kola</li>
    <li>Peak Mist</li>
  </ul>
  <ul class="list" style="left:631px; top:757px;">
    <li>Diet Mist</li>
    <li>Lemonade</li>
    <li>Lime Lift</li>
    <li>Dr Bramble</li>
  </ul>
  <div class="art art-cup" role="img" aria-label="Soft drink cup icon goes here"></div>

  <h2 class="tag tag-shake">Shake</h2>
  <div class="art art-shake" role="img" aria-label="Milkshake glass icon goes here"></div>
  <ul class="list list-right" style="right:44px; top:960px;">
    <li>Rick's Signature Raspberry Jammin Shake</li>
    <li>Raspberry Cookie Crumble Shake</li>
    <li>Raspberry Cocoa Hazel Bomb Shake</li>
    <li>Raspberry Beachin' Shake<small>(Pina Colada)</small></li>
    <li>Raspberry Brownies Shake</li>
    <li>Caramel Shake</li>
    <li>Chocolate Shake</li>
  </ul>
</main>
</body>
</html>
```